TLR Property - Business Cards

Looking for a business card & general letterhead, signage etc design for our new logo.

Colours:
000a20
0056a2
00b5ef
0088ce
68cef2

Fonts:
Poppins
Karla

Please keep look and feel of new brand - example in the zip package I sent.

```html
<!DOCTYPE html>
<html lang="en">
<head>
<meta charset="utf-8">
<title>TLR Property – Business Cards</title>
<link rel="stylesheet" href="https://fonts.googleapis.com/css2?family=Poppins:wght@400;500;700;800&display=swap">
<style>
  :root {
    --navy: #000a20;
    --navy-card: #0b1130;
    --blue-deep: #0056a2;
    --blue-mid: #0088ce;
    --blue-bright: #00b5ef;
    --blue-soft: #68cef2;
    --paper: #ffffff;
    --ink: #111111;
    --stage: #3b3b3d;
  }
  * { box-sizing: border-box; margin: 0; padding: 0; }
  html, body {
    width: 1200px; height: 900px; overflow: hidden;
    background: var(--stage);
    font-family: "Poppins", sans-serif;
  }
  .sheet {
    width: 1200px; height: 900px;
    display: flex; flex-direction: column;
    align-items: center; justify-content: center; gap: 44px;
  }
  .card {
    position: relative;
    width: 600px; height: 343px;
    border-radius: 22px;
    overflow: hidden;
  }
  /* Back side */
  .card--back { background: var(--navy-card); }
  .card--back .brand {
    position: absolute; right: 62px; top: 128px;
    display: flex; align-items: center; gap: 14px;
  }
  .brand-dot {
    width: 30px; height: 30px; border-radius: 50%;
    background: var(--blue-bright);
  }
  .brand-name {
    font-weight: 800; font-size: 46px; line-height: 1;
    letter-spacing: 1px; color: var(--paper);
  }
  /* Front side */
  .card--front { background: var(--paper); }
  .card--front .brand {
    position: absolute; left: 40px; top: 36px;
    display: flex; align-items: center; gap: 10px;
  }
  .card--front .brand-dot { width: 22px; height: 22px; background: var(--blue-bright); }
  .card--front .brand-name { font-size: 32px; color: var(--blue-deep); }
  .contact {
    position: absolute; left: 40px; top: 142px;
    list-style: none; color: var(--ink);
    font-size: 15px; line-height: 22px;
  }
  .contact li { display: flex; align-items: center; gap: 7px; }
  .contact svg { width: 12px; height: 12px; flex: none; }
  .address {
    position: absolute; left: 40px; top: 222px;
    font-size: 15px; line-height: 22px; color: var(--ink);
    font-style: normal;
  }
  .holder {
    position: absolute; right: 42px; top: 150px; text-align: left;
  }
  .holder-name {
    font-weight: 800; font-size: 30px; line-height: 1.05;
    color: var(--blue-deep); letter-spacing: 0.5px;
    white-space: nowrap;
  }
  .holder-name .surname { color: var(--blue-mid); }
  .holder-role {
    font-size: 16px; color: var(--ink); margin-top: 2px; padding-left: 22px;
  }
  .edge-tab {
    position: absolute; right: 0; top: 150px;
    width: 14px; height: 50px;
    background: var(--blue-deep);
    border-radius: 8px 0 0 8px;
  }
</style>
</head>
<body>
<main class="sheet">
  <section class="card card--back" aria-label="Business card back">
    <div class="brand">
      <span class="brand-dot"></span>
      <span class="brand-name">TLR PROPERTY</span>
    </div>
  </section>

  <section class="card card--front" aria-label="Business card front">
    <div class="brand">
      <span class="brand-dot"></span>
      <span class="brand-name">TLR PROPERTY</span>
    </div>

    <ul class="contact">
      <li>
        <svg viewBox="0 0 12 12" aria-hidden="true"><path d="M3 1l2 2.5-1.2 1.3a7 7 0 0 0 3.4 3.4L8.5 7 11 9l-1 2C5 11 1 7 1 2z" fill="var(--blue-deep)"/></svg>
        +1- 415-555-0148
      </li>
      <li>
        <svg viewBox="0 0 12 12" aria-hidden="true"><rect x="0.8" y="2.5" width="10.4" height="7" fill="none" stroke="var(--blue-deep)" stroke-width="1.2"/><path d="M1 3l5 3.5L11 3" fill="none" stroke="var(--blue-deep)" stroke-width="1.2"/></svg>
        info@tlrproperty.com
      </li>
      <li>
        <svg viewBox="0 0 12 12" aria-hidden="true"><circle cx="6" cy="6" r="5" fill="var(--blue-deep)"/><path d="M1 6h10M6 1v10" stroke="#fff" stroke-width="0.8"/></svg>
        www.tlrproperty.com
      </li>
    </ul>

    <address class="address">
      2140 North Elm Avenue<br>
      #18, Suite Lakewood
    </address>

    <div class="holder">
      <p class="holder-name">MAREN <span class="surname">TOLVIK</span></p>
      <p class="holder-role">Founder &amp; Principal</p>
    </div>

    <span class="edge-tab"></span>
  </section>
</main>
</body>
</html>
```